Animal Eye Clinic needs a Business card

We are a new veterinary ophthalmology practice (Tessaly Animal Eye Care) and we need a business card designed. We only see animal eyes - we are not a regular veterinary clinic. We already have a logo. We are looking for a professional, good looking business card to hand out to our clients. We are looking for something simple but professional and contemporary. Our logo is likely the only picture/graphic that needs to be on the card.
Updates

Contact Information for Business Card

Marisol Dunkley, BSc, DVM, MSc, DipACVO
Veterinary Ophthalmologist

Phone: 250.418.3097
Email: tessalyanimaleyecare@mailbrook.net
Website: tessalyanimaleyecare.net
Address: 1840 Pellworth Rd
Kelowna, BC, V4T 8M3

Colors

Designer to choose colors to be used in the design.

Requirements
Must have
• Our logo (attached)

```html
<!DOCTYPE html>
<html lang="en">
<head>
<meta charset="utf-8">
<title>Tessaly Animal Eye Care – Business Card</title>
<link rel="stylesheet" href="https://fonts.googleapis.com/css2?family=Open+Sans:wght@400;600;700&display=swap">
<style>
  :root {
    --teal: #0596a9;
    --grey: #7a7a7a;
    --white: #ffffff;
    --paper: #f4f4f4;
    --backdrop: #d9d9d9;
  }
  * { box-sizing: border-box; margin: 0; padding: 0; }
  html, body {
    width: 1200px; height: 800px; overflow: hidden;
    background: var(--backdrop);
    font-family: "Open Sans", Arial, sans-serif;
  }
  .canvas {
    position: relative; width: 1200px; height: 800px;
    display: flex; flex-direction: column; align-items: center; justify-content: center; gap: 40px;
  }
  .card {
    position: relative; width: 600px; height: 340px;
    border-radius: 22px; overflow: hidden;
    box-shadow: 0 6px 18px rgba(0,0,0,0.18);
  }

  /* Back: contact side */
  .card--contact { background: var(--teal); color: var(--white); }
  .contact__wash {
    position: absolute; right: -80px; top: -140px;
    width: 340px; height: 340px; border-radius: 50%;
    background: var(--white);
  }
  .contact__emblem {
    position: absolute; right: 30px; top: 36px;
    width: 230px; height: 230px; border-radius: 50%;
    border: 10px solid var(--white);
    background: var(--teal);
  }
  .contact__body { position: absolute; left: 44px; top: 54px; width: 280px; }
  .contact__brand {
    font-size: 18px; font-weight: 600; letter-spacing: 1px;
    text-transform: uppercase; line-height: 1.25; margin-bottom: 30px;
  }
  .contact__name { font-size: 14px; font-weight: 700; text-transform: uppercase; letter-spacing: 0.3px; white-space: nowrap; }
  .contact__creds { font-size: 10px; font-weight: 600; text-transform: none; letter-spacing: 0; }
  .contact__role { font-size: 13px; margin-bottom: 14px; }
  .contact__address { font-size: 13px; line-height: 1.35; margin-bottom: 6px; }
  .contact__list { list-style: none; font-size: 13px; line-height: 1.5; }
  .contact__list li { display: flex; align-items: center; gap: 8px; white-space: nowrap; }
  .contact__list svg { width: 12px; height: 12px; flex: none; }

  /* Front: brand side */
  .card--brand { background: var(--paper); display: flex; align-items: center; justify-content: center; }
  .brand { display: flex; align-items: center; gap: 16px; }
  .brand__dot { width: 54px; height: 54px; border-radius: 50%; background: var(--teal); flex: none; }
  .brand__name { font-size: 32px; font-weight: 600; color: var(--teal); letter-spacing: 0.5px; white-space: nowrap; }
</style>
</head>
<body>
<main class="canvas">
  <section class="card card--contact">
    <div class="contact__wash"></div>
    <div class="contact__emblem" role="img" aria-label="Clinic emblem area: horse, dog and cat within a circle"></div>
    <div class="contact__body">
      <p class="contact__brand">Tessaly<br>Animal Eye Care</p>
      <p class="contact__name">Marisol Dunkley, <span class="contact__creds">BSc, DVM, MSc, DipACVO</span></p>
      <p class="contact__role">Veterinary Ophthalmologist</p>
      <p class="contact__address">1840 Pellworth Rd<br>Kelowna, BC, V4T 8M3</p>
      <ul class="contact__list">
        <li>
          <svg viewBox="0 0 12 12" aria-hidden="true"><path fill="#fff" d="M2.5 0.8l2 2-1 1.3c.7 1.5 1.9 2.7 3.4 3.4l1.3-1 2 2-1.2 1.7C5 10 2 7 .8 2z"/></svg>
          250.418.3097
        </li>
        <li>
          <svg viewBox="0 0 12 12" aria-hidden="true"><rect x="0.5" y="2" width="11" height="8" rx="1" fill="#fff"/><path d="M1 2.7l5 3.8 5-3.8" stroke="#0596a9" stroke-width="1" fill="none"/></svg>
          tessalyanimaleyecare@mailbrook.net
        </li>
        <li>
          <svg viewBox="0 0 12 12" aria-hidden="true"><circle cx="6" cy="6" r="5.5" fill="#fff"/><path d="M0.8 6h10.4M6 .6c-2.4 3-2.4 7.8 0 10.8M6 .6c2.4 3 2.4 7.8 0 10.8" stroke="#0596a9" stroke-width="0.9" fill="none"/></svg>
          tessalyanimaleyecare.net
        </li>
      </ul>
    </div>
  </section>

  <section class="card card--brand">
    <div class="brand">
      <span class="brand__dot"></span>
      <p class="brand__name">Tessaly Animal Eye Care</p>
    </div>
  </section>
</main>
</body>
</html>
```